As a dynamic multi-disciplinary care centre, Brindlewood Spinal Vitality Centre has been serv...

We need a vibrant, welcoming brochure that introduces our centre to the local communities. I would prefer a simple one page (brochure sized postcard - single or double sided depending on layout for content). Our services and products include Chiropractic (primary service of the centre), Massage Therapy, Acupuncture, Custom Orthotics, and Nutritional Supplements. We are wellness based, primarily serving active families to maximize their health potential as indicated in our Mission Statement:"Our Mission is to empower individuals of all ages to maximize their God given health potential. We are committed to delivering a unique wellness experience with compassion, integrity and ultimate respect, while inspiring our clients to lead a lifestyle that embraces the philosophy that health comes from within.”I'm attaching our logo, and our website is www.thrivehomeclinic.example

We need our contact information included: #418 - 37 Quillmere Crescent SE Calgary, AB, T3K 5N2 Phone: 403-555-0174 Website: www.thrivehomeclinic.example Facebook: www.facebook.example/BrindlewoodSpinal Instagram: www.instagram.example/Brindlewood_Spinal

Target Market(s)

Active families looking to maximize their health. Our tagline is - "Maximizing Health...Inspiring Life"

Industry/Entity Type

Health And Wellness

Font styles to use
Sans Serif

Colors
85abd2
3276b5
0655a3

Requirements
Must have
• Image that exemplifies health and active lifestyle.
• Listing of services and products.
• Contact information.
Nice to have
• Tagline or Mission Statement

```html
<!DOCTYPE html>
<html lang="en">
<head>
<meta charset="utf-8">
<title>Brindlewood Spinal Vitality Centre – Flyer</title>
<link rel="stylesheet" href="https://fonts.googleapis.com/css2?family=Roboto:wght@300;400;500;700;900&display=swap">
<style>
  :root {
    --navy-blue: #0655a3;
    --mid-blue: #3276b5;
    --sky-blue: #85abd2;
    --cyan: #1ea3e0;
    --grey-light: #f1f1f2;
    --grey-mid: #dcdcde;
    --charcoal: #2f2f31;
    --text-dark: #3a3a3c;
    --white: #ffffff;
    --stage: #e8e6e3;
  }
  * { box-sizing: border-box; margin: 0; padding: 0; }
  html, body {
    width: 1200px; height: 1200px; overflow: hidden;
    background: var(--stage);
    font-family: "Roboto", Arial, sans-serif;
  }
  .flyer {
    position: absolute; left: 204px; top: 40px;
    width: 792px; height: 1120px;
    overflow: hidden;
    background: var(--grey-light);
    box-shadow: 0 10px 30px rgba(0,0,0,.18);
  }
  .hero-photo {
    position: absolute; left: 0; top: 0; width: 792px; height: 640px;
    background:
      radial-gradient(circle at 72% 8%, #ffe27a 0%, rgba(255,200,70,.6) 12%, rgba(255,200,70,0) 32%),
      linear-gradient(180deg, #3f7d2a 0%, #5fa53a 40%, #7fcf4e 70%, #9bd865 100%);
  }
  .flyer-shapes { position: absolute; left: 0; top: 0; }

  .brand {
    position: absolute; left: 34px; top: 92px;
    display: flex; align-items: center; gap: 12px;
  }
  .brand-dot {
    width: 46px; height: 46px; border-radius: 50%;
    background: var(--cyan);
  }
  .brand-name {
    font-weight: 700; font-size: 22px; line-height: 1.1;
    color: var(--navy-blue);
  }

  .intro-card {
    position: absolute; left: 44px; top: 640px;
    width: 360px; height: 262px;
    background: var(--navy-blue);
    border: 4px solid var(--white);
    border-radius: 14px;
    box-shadow: 0 8px 18px rgba(0,0,0,.25);
    padding: 20px 22px;
    color: var(--white);
  }
  .section-title {
    font-weight: 900; font-size: 19px; line-height: 1.02;
    text-transform: uppercase;
    border-left: 3px solid currentColor;
    padding-left: 8px;
    margin-bottom: 10px;
  }
  .intro-card p {
    font-weight: 300; font-size: 13.5px; line-height: 1.3;
    margin-bottom: 12px;
  }
  .service-list {
    list-style: none;
    display: grid; grid-template-columns: 1fr 1fr; gap: 3px 10px;
    font-weight: 700; font-size: 13px;
  }
  .service-list li::before {
    content: ""; display: inline-block; width: 6px; height: 6px;
    background: var(--white); margin-right: 5px; vertical-align: middle;
  }
  .service-list .wide { grid-column: 1 / span 2; }

  .about {
    position: absolute; left: 430px; top: 480px; width: 330px;
    color: var(--text-dark);
  }
  .about .section-title { color: var(--navy-blue); }
  .about p {
    font-weight: 400; font-size: 13px; line-height: 1.35;
    margin-bottom: 12px;
  }
  .about strong { color: var(--navy-blue); font-weight: 700; }

  .contact-block { position: absolute; color: var(--white); }
  .contact-label {
    font-weight: 700; font-size: 17px; text-transform: uppercase;
    color: var(--cyan);
  }
  .call-us { left: 44px; top: 1030px; }
  .call-us .phone { font-weight: 700; font-size: 24px; }
  .visit-us { left: 330px; top: 975px; }
  .visit-us .address { font-weight: 700; font-size: 12.5px; line-height: 1.3; }
  .connect { left: 560px; top: 895px; }
  .social-row { display: flex; gap: 12px; margin-top: 6px; }
  .social-row span {
    width: 16px; height: 16px; border-radius: 50%;
    background: var(--white);
  }
</style>
</head>
<body>
<main class="flyer">
  <div class="hero-photo" role="img" aria-label="Photo of a smiling couple jogging along a sunlit grassy park trail"></div>

  <svg class="flyer-shapes" width="792" height="1120" viewBox="0 0 792 1120" aria-hidden="true">
    <!-- header corner -->
    <path d="M0 0 H462 C420 135 270 228 0 252 Z" fill="var(--cyan)"/>
    <path d="M0 0 H448 C405 125 260 214 0 238 Z" fill="var(--navy-blue)"/>
    <path d="M0 0 H432 C390 115 250 202 0 224 Z" fill="var(--white)"/>
    <!-- middle section -->
    <path d="M0 576 C200 536 350 496 470 416 C580 346 700 356 792 376 V1120 H0 Z" fill="var(--cyan)"/>
    <path d="M0 592 C200 552 350 512 470 432 C580 362 700 372 792 392 V1120 H0 Z" fill="var(--navy-blue)"/>
    <defs>
      <linearGradient id="greyPanel" x1="0" y1="0" x2="1" y2="1">
        <stop offset="0" stop-color="#dadadc"/>
        <stop offset="0.5" stop-color="#f4f4f5"/>
        <stop offset="1" stop-color="#e2e2e4"/>
      </linearGradient>
    </defs>
    <path d="M0 600 C200 560 350 520 470 440 C580 370 700 380 792 400 V1120 H0 Z" fill="url(#greyPanel)"/>
    <!-- footer band -->
    <path d="M0 994 C220 974 420 914 560 854 C660 814 730 804 792 799 V1120 H0 Z" fill="var(--cyan)"/>
    <path d="M0 1002 C220 982 420 922 560 862 C660 822 730 812 792 807 V1120 H0 Z" fill="var(--navy-blue)"/>
    <path d="M0 1010 C220 990 420 930 560 870 C660 830 730 820 792 815 V1120 H0 Z" fill="var(--charcoal)"/>
  </svg>

  <div class="brand">
    <span class="brand-dot"></span>
    <div class="brand-name">Brindlewood Spinal<br>Vitality Centre</div>
  </div>

  <section class="intro-card">
    <h2 class="section-title">Maximizing Health…<br>Inspiring Life</h2>
    <p>We are here to help you live a fulfilling, vibrant life, allowing you to participate in the activities you love with the people you care about.</p>
    <p>Our centre offers quality care in the services of…</p>
    <ul class="service-list">
      <li>Chiropractic</li>
      <li>Massage Therapy</li>
      <li>Acupuncture</li>
      <li>Custom Orthotics</li>
      <li class="wide">Nutritional Supplements</li>
    </ul>
  </section>

  <section class="about">
    <h2 class="section-title">Chiropractic Centre for<br>Family Wellness</h2>
    <p>Brindlewood Spinal Vitality Centre has been serving the communities of south Calgary with excellent natural health care since 2001.</p>
    <p>We are committed to delivering a unique wellness experience with compassion, integrity, and ultimate respect, while inspiring our clients to lead a lifestyle that embraces the philosophy the health comes from within.</p>
    <p>Our chiropractors, <strong>Dr. Owen Tallisker</strong> and <strong>Dr. Reid Vanholm</strong>, use state-of-the-art technology and techniques designed to maximize your health.</p>
  </section>

  <div class="contact-block call-us">
    <div class="contact-label">Call Us Today</div>
    <div class="phone">(403) 555-0174</div>
  </div>
  <div class="contact-block visit-us">
    <div class="contact-label">Visit Us</div>
    <div class="address">418-37 Quillmere Cres SE<br>Calgary, AB T3K 5N2</div>
  </div>
  <div class="contact-block connect">
    <div class="contact-label">Connect With Us</div>
    <div class="social-row"><span></span><span></span><span></span><span></span></div>
  </div>
</main>
</body>
</html>
```